Cannabis company needs an e-commerce website

Our retail cannabis company Vale Ember needs a fully functioning e-commerce website optimized for SEO. We want the website to have the appeal and sophistication of a cigar lounge/boutique coffee shop highlighting our high-end artisanal products. It should have the ability to categorize and search for products based on tags. Our initial number of SKUs will be about 25, but that will grow as the business grows.

Target Market(s)

Online retail cannabis users

Industry/Entity Type

Cannabis

Coding

Coded - Design and coding required

Number of Pages Required

5+ page

Font styles to use
Sans Serif

Requirements
Must have
• - Age confirmation (19+) confirmation popup
- Very simple and easy method of purchasing based on different product sizes
- Search functionality based on tags etc. of the products
- Similar functionality to the following websites:
1) https://www.fernbrookherbals.com/
2) https://mossparlor.io/
3) https://lunatrove.org/
4) https://plumcurio.com/
- Similar look to the following websites:
1) https://layoutbazaar.net/item/corvin-pipe-shop-theme/48203917
2) https://www.bramsoil.ca/
3) https://dunmoorguild.org/
4) https://wrenfieldapothecary.com/

```html
<!DOCTYPE html>
<html lang="en">
<head>
<meta charset="utf-8">
<title>Vale Ember – Collection</title>
<link href="https://fonts.googleapis.com/css2?family=Lato:wght@400;700;900&display=swap" rel="stylesheet">
<style>
:root{
  --bar:#1f1f1f;
  --page:#2b2b2b;
  --band:#242424;
  --footer:#222222;
  --line:#3b3b3b;
  --text:#ffffff;
  --muted:#cfcfcf;
  --dim:#9a9a9a;
  --star:#f7a21b;
  --red:#e01616;
  --sw1:#cfe9fb;
  --sw2:#f1e3e0;
  --sw3:#bdbdbd;
  --tile:#ececec;
}
*{margin:0;padding:0;box-sizing:border-box}
html,body{width:811px;height:1200px;overflow:hidden;background:var(--page)}
body{font-family:"Lato",sans-serif;color:var(--text)}
.canvas{position:relative;width:811px;height:1200px;overflow:hidden;background:var(--page)}
.abs{position:absolute}
.topbar{left:0;top:0;width:811px;height:21px;background:var(--bar);font-size:7px}
.topbar span{position:absolute;top:6px;white-space:nowrap}
.header{left:0;top:21px;width:811px;height:111px;background:var(--page)}
.logo{font-weight:900;letter-spacing:1.5px;text-align:center;white-space:nowrap}
.nav a{position:absolute;top:111px;font-size:8.3px;letter-spacing:.6px;color:var(--text);text-decoration:none}
.nav svg{position:absolute;top:114px}
.crumbband{left:0;top:132px;width:811px;height:53px;background:var(--band)}
.crumbband .title{position:absolute;left:58px;top:22px;font-size:8.3px;font-weight:700}
.crumbband .path{position:absolute;right:58px;top:22px;font-size:7.5px;font-weight:700}
.sidebar{left:58px;top:220px;width:162px;height:337px;border:1px solid var(--line)}
.facet{position:absolute;left:16px;font-size:8px;font-weight:700;letter-spacing:.3px}
.caret{position:absolute;left:143px;width:0;height:0;border-left:3px solid transparent;border-right:3px solid transparent;border-top:3.5px solid #fff}
.opt{position:absolute;left:16px;font-size:5.8px;color:var(--muted);display:flex;align-items:center;gap:5px}
.opt i{display:block;width:7px;height:7px;background:#fff;border-radius:1.5px}
.sectionhead{left:58px;top:571px;font-size:8.3px;font-weight:700;letter-spacing:.3px}
.mini{position:absolute;left:58px;width:48px;height:66px}
.miniinfo{position:absolute;left:114px}
.stars{color:var(--star);font-size:6.5px;letter-spacing:1.6px}
.stars b{color:#ddd;font-weight:400}
.pname{font-size:7px;color:var(--muted)}
.price{font-size:10px;font-weight:700}
.banner{left:236px;top:220px;width:517px;height:146px;background:linear-gradient(90deg,#e9e6df 0%,#d8d4c8 30%,#ebe9e4 55%,#dfe3de 100%)}
.bottle{left:322px;top:220px;width:70px;height:146px;background:linear-gradient(180deg,#b99a33,#f0c419 45%,#e3b20f);opacity:.95}
.leaf{left:440px;top:300px;width:313px;height:66px;background:linear-gradient(100deg,rgba(46,120,60,.0) 0%,rgba(46,120,60,.85) 40%,rgba(36,100,48,.7) 100%);border-radius:70% 0 0 0}
.banner-title{left:401px;top:260px;font-size:11px;color:#333}
.banner-sub{left:402px;top:285px;font-size:7.3px;color:#333}
.copyhead{left:236px;top:382px;font-size:10px}
.copylead{left:236px;top:401px;font-size:7.8px;font-weight:700;letter-spacing:.3px}
.copybody{left:236px;top:416px;width:517px;font-size:6.7px;line-height:10.6px;color:#e4e4e4;white-space:nowrap}
.toolbar{left:236px;top:475px;width:517px;height:34px;border-top:1px solid var(--line);border-bottom:1px solid var(--line)}
.toolbar .sep{position:absolute;top:0;width:1px;height:33px;background:var(--line)}
.toolbar .t{position:absolute;top:12px;font-size:7px;color:var(--muted)}
.card{position:absolute;width:73px}
.card .img{width:73px;height:94px;background:var(--tile);position:relative;overflow:hidden}
.card .img span{position:absolute;left:18px;top:16px;width:37px;height:60px;border-radius:4px}
.card .meta{margin-left:2px}
.card .stars{margin-top:5px;line-height:7px}
.card .pname{line-height:9px;font-size:6.8px}
.card .price{line-height:12px}
.swatches{display:flex;gap:4px;margin-top:5px}
.swatches i{width:10px;height:10px;border-radius:50%;display:block}
.pager{left:236px;top:886px;width:517px;height:28px;border:1px solid var(--line)}
.pager .cell{position:absolute;top:0;height:26px;border-right:1px solid var(--line);font-size:7px;color:var(--dim);display:flex;align-items:center;justify-content:center}
.pager .result{position:absolute;right:8px;top:9px;font-size:7px;color:var(--muted)}
.footer{left:0;top:975px;width:811px;height:225px;background:var(--footer)}
.fcol{position:absolute;text-align:center}
.about{white-space:nowrap}
.vline{position:absolute;top:1010px;width:1px;height:98px;background:var(--line)}
.news-input{left:292px;top:1049px;width:227px;height:25px;border:1px solid #444;font-size:6px;letter-spacing:3px;color:#888;text-align:center;line-height:23px}
.subscribe{left:370px;top:1080px;width:71px;height:24px;border:1px solid #ddd;font-size:6.8px;font-weight:700;text-align:center;line-height:22px}
.info p{font-size:6.8px;line-height:15.3px}
.bottomline{left:52px;top:1163px;width:708px;height:1px;background:var(--line)}
.pay{position:absolute;top:1174px;width:14px;height:14px;border-radius:50%}
</style>
</head>
<body>
<div class="canvas">

  <div class="abs topbar">
    <span style="left:58px">Welcome to Our store Vale Ember</span>
    <span style="left:168px">
      <svg width="6" height="6" viewBox="0 0 10 10" style="vertical-align:-1px"><path d="M2 1l2 2-1 1.5c.7 1.5 1.8 2.6 3.3 3.3L7.8 6.8l2 2-1.3 1.2C4.5 9.6.4 5.5 0 1.5z" fill="#fff"/></svg>
      &nbsp;Call Us: 123 - 456 - 7890</span>
    <span style="left:630px">&#9829; Wishlist</span>
    <span style="left:694px">&#9679; My Account &nbsp;&#709;</span>
  </div>

  <div class="abs header">
    <svg class="abs" style="left:58px;top:34px" width="13" height="10" viewBox="0 0 13 10"><rect width="13" height="1.8" fill="#fff"/><rect y="4" width="13" height="1.8" fill="#fff"/><rect y="8" width="13" height="1.8" fill="#fff"/></svg>
    <div class="abs logo" style="left:318px;top:28px;width:140px;font-size:18px">VALE EMBER</div>
    <svg class="abs" style="left:694px;top:33px" width="12" height="12" viewBox="0 0 12 12"><circle cx="5" cy="5" r="4" fill="none" stroke="#fff" stroke-width="1.2"/><line x1="8" y1="8" x2="11.5" y2="11.5" stroke="#fff" stroke-width="1.3"/></svg>
    <svg class="abs" style="left:717px;top:33px" width="13" height="13" viewBox="0 0 13 13"><circle cx="6.5" cy="6.5" r="4.6" fill="none" stroke="#fff" stroke-width="1" stroke-dasharray="2 1.2"/><circle cx="6.5" cy="6.5" r="2" fill="none" stroke="#fff" stroke-width="1"/></svg>
    <svg class="abs" style="left:741px;top:33px" width="12" height="12" viewBox="0 0 12 12"><path d="M1 4.5h10l-1 7H2z" fill="none" stroke="#fff" stroke-width="1"/><path d="M3.5 4.5L6 1l2.5 3.5" fill="none" stroke="#fff" stroke-width="1"/><line x1="4.5" y1="6.5" x2="4.5" y2="10" stroke="#fff" stroke-width=".8"/><line x1="7.5" y1="6.5" x2="7.5" y2="10" stroke="#fff" stroke-width=".8"/></svg>
    <div class="abs" style="left:58px;top:78px;width:695px;height:1px;background:var(--line)"></div>
  </div>

  <nav class="nav">
    <a style="left:225px">HOME</a>
    <a style="left:274px">SHOP</a><svg style="left:305px" width="5" height="4" viewBox="0 0 5 4"><path d="M.5.5l2 2 2-2" stroke="#fff" fill="none"/></svg>
    <a style="left:322px">ABOUT</a>
    <a style="left:375px">PRODUCT</a><svg style="left:424px" width="5" height="4" viewBox="0 0 5 4"><path d="M.5.5l2 2 2-2" stroke="#fff" fill="none"/></svg>
    <a style="left:440px">BRANDS</a><svg style="left:483px" width="5" height="4" viewBox="0 0 5 4"><path d="M.5.5l2 2 2-2" stroke="#fff" fill="none"/></svg>
    <a style="left:499px">BLOG</a>
    <a style="left:546px">FAQ</a>
  </nav>

  <div class="abs crumbband">
    <div class="title">COLLECTION</div>
    <div class="path">HOME <span style="color:#777;font-weight:400">&nbsp;/&nbsp;</span> COLLECTION</div>
  </div>

  <aside class="abs sidebar">
    <div class="facet" style="top:17px">BRAND</div><div class="caret" style="top:19px"></div>
    <div class="opt" style="top:43px"><i></i>BRAND</div>
    <div class="opt" style="top:61px"><i></i>BRAND</div>
    <div class="opt" style="top:79px"><i></i>BRAND</div>
    <div class="opt" style="top:98px"><i></i>BRAND</div>
    <div class="opt" style="top:116px"><i></i>BRAND</div>
    <div class="facet" style="top:154px">SIZE</div><div class="caret" style="top:156px"></div>
    <div class="opt" style="top:180px"><i></i>S</div>
    <div class="opt" style="top:198px"><i></i>M</div>
    <div class="opt" style="top:216px"><i></i>L</div>
    <div class="opt" style="top:235px"><i></i>XL</div>
    <div class="facet" style="top:274px">PRICE</div><div class="caret" style="top:276px"></div>
    <div class="abs" style="left:18px;top:291px;font-size:5px;color:#777">$0</div>
    <div class="abs" style="left:124px;top:288px;font-size:5.5px;font-weight:700;background:var(--red);padding:1px 2px;border-radius:1px">$1.500</div>
    <div class="abs" style="left:16px;top:305px;width:129px;height:3px;background:var(--red);border-radius:2px"></div>
    <div class="abs" style="left:19px;top:303px;width:125px;height:1px;background:#fff"></div>
  </aside>

  <div class="abs sectionhead">NEW PRODUCT</div>
  <svg class="abs" style="left:197px;top:569px" width="24" height="11" viewBox="0 0 24 11"><circle cx="5" cy="5.5" r="5" fill="#777"/><path d="M6 3l-2 2.5 2 2.5" stroke="#2b2b2b" fill="none"/><circle cx="18.5" cy="5.5" r="5" fill="#777"/><path d="M17.5 3l2 2.5-2 2.5" stroke="#2b2b2b" fill="none"/></svg>
  <div class="abs" style="left:58px;top:587px;width:162px;height:1px;background:var(--line)"></div>

  <div class="mini" role="img" aria-label="Photo of cannabis oil bottles with hemp leaves" style="top:599px;background:linear-gradient(135deg,#6f8a2c,#b8c24a 50%,#4f6a22)"></div>
  <div class="miniinfo" style="top:614px"><div class="stars">★★★★<b>★</b></div><div class="pname">Cannabis Product</div><div class="price">$500.00</div></div>
  <div class="mini" role="img" aria-label="Photo of ground cannabis in a glass dish" style="top:680px;background:linear-gradient(135deg,#3a2a12,#8a6a2a 50%,#2a1c0c)"></div>
  <div class="miniinfo" style="top:695px"><div class="stars">★★★★<b>★</b></div><div class="pname">Cannabis Product</div><div class="price">$500.00</div></div>
  <div class="mini" role="img" aria-label="Photo of cannabis buds on wood" style="top:761px;background:linear-gradient(135deg,#8a6a40,#5d6a34 50%,#a07a4a)"></div>
  <div class="miniinfo" style="top:776px"><div class="stars">★★★★<b>★</b></div><div class="pname">Cannabis Product</div><div class="price">$500.00</div></div>

  <div class="abs banner" role="img" aria-label="Photo of a cannabis oil bottle beside a cannabis leaf"></div>
  <div class="abs bottle" aria-hidden="true"></div>
  <div class="abs leaf" aria-hidden="true"></div>
  <div class="abs banner-title">CANNABIS OIL</div>
  <div class="abs banner-sub">LOREM IPSUM IS SIMPLY DUMMY TEXT OF THE PRINTING AND TYPESETTING INDUSTRY.</div>

  <h1 class="abs copyhead" style="font-weight:400">Cannabis Oil</h1>
  <div class="abs copylead">Lorem Ipsum is simply dummy text of the printing and typesetting industry.</div>
  <p class="abs copybody">Lorem Ipsum is simply dummy text of the printing and typesetting industry. Lorem Ipsum has been the industry's standard dummy text ever since the 1500s, when an<br>unknown printer took a galley of type and scrambled it to make a type specimen book. It has survived not only five centuries, but also the leap into electronic typesetting,<br>remaining essentially unchanged. It was popularised in the 1960s with the release of Tessaline sheets containing Lorem Ipsum passages, and more recently with desktop<br>publishing software like Quillform Pages including versions of Lorem Ipsum.</p>

  <div class="abs toolbar">
    <div class="t" style="left:10px;font-size:7.8px;color:#eee;top:11px;letter-spacing:.2px">Showing Products 1-24 Of 10 Result</div>
    <div class="sep" style="left:180px"></div>
    <svg class="abs" style="left:190px;top:14px" width="26" height="7" viewBox="0 0 26 7"><g fill="#fff"><rect x="0" y="0" width="2" height="2"/><rect x="2.5" y="0" width="2" height="2"/><rect x="5" y="0" width="2" height="2"/><rect x="0" y="2.5" width="2" height="2"/><rect x="2.5" y="2.5" width="2" height="2"/><rect x="5" y="2.5" width="2" height="2"/><rect x="0" y="5" width="2" height="2"/><rect x="2.5" y="5" width="2" height="2"/><rect x="5" y="5" width="2" height="2"/><rect x="16" y="0.5" width="1.2" height="1.2"/><rect x="18" y="0.5" width="6" height="1.2"/><rect x="16" y="3" width="1.2" height="1.2"/><rect x="18" y="3" width="6" height="1.2"/><rect x="16" y="5.5" width="1.2" height="1.2"/><rect x="18" y="5.5" width="6" height="1.2"/></g></svg>
    <svg class="abs" style="left:248px;top:13px" width="77" height="8" viewBox="0 0 77 8"><g fill="#fff"><rect x="0" width="3" height="8"/><rect x="4.5" width="3" height="8"/><rect x="14" width="2.5" height="8"/><rect x="18" width="2.5" height="8"/><rect x="22" width="2.5" height="8"/><rect x="34" width="2" height="8"/><rect x="37.5" width="2" height="8"/><rect x="41" width="2" height="8"/><rect x="44.5" width="2" height="8"/><rect x="55" width="1.8" height="8"/><rect x="58" width="1.8" height="8"/><rect x="61" width="1.8" height="8"/><rect x="64" width="1.8" height="8"/><rect x="67" width="1.8" height="8"/><rect x="70" width="1.8" height="8"/></g></svg>
    <div class="sep" style="left:335px"></div>
    <div class="t" style="left:346px">24 Products Par Page</div>
    <div class="abs" style="left:428px;top:15px;border-left:2.5px solid transparent;border-right:2.5px solid transparent;border-top:3px solid #aaa"></div>
    <div class="sep" style="left:439px"></div>
    <div class="t" style="left:449px">Sorting items</div>
    <div class="abs" style="left:508px;top:15px;border-left:2.5px solid transparent;border-right:2.5px solid transparent;border-top:3px solid #aaa"></div>
  </div>

  <!-- first product row -->
  <div class="card" style="left:236px;top:535px"><div class="img" role="img" aria-label="Product photo: dark box with a serum vial"><span style="background:linear-gradient(180deg,#e6c84a 0 18%,#1e2238 18%)"></span></div><div class="meta"><div class="stars">★★★★<b>★</b></div><div class="pname">Cannabis Product</div><div class="price">$500.00</div><div class="swatches"><i style="background:var(--sw1)"></i><i style="background:var(--sw2)"></i><i style="background:var(--sw3)"></i></div></div></div>
  <div class="card" style="left:324px;top:535px"><div class="img" role="img" aria-label="Product photo: green box and blue dropper bottle"><span style="background:linear-gradient(90deg,#2f7a3a,#5aa85e 55%,#23358a 55%)"></span></div><div class="meta"><div class="stars">★★★★<b>★</b></div><div class="pname">Cannabis Product</div><div class="price">$500.00</div><div class="swatches"><i style="background:var(--sw1)"></i><i style="background:var(--sw2)"></i><i style="background:var(--sw3)"></i></div></div></div>
  <div class="card" style="left:413px;top:535px"><div class="img" role="img" aria-label="Product photo: bag of edibles beside black pouch"><span style="background:linear-gradient(90deg,#c9a06a 45%,#262626 45%)"></span></div><div class="meta"><div class="stars">★★★★<b>★</b></div><div class="pname">Cannabis Product</div><div class="price">$500.00</div><div class="swatches"><i style="background:var(--sw1)"></i><i style="background:var(--sw2)"></i><i style="background:var(--sw3)"></i></div></div></div>
  <div class="card" style="left:502px;top:535px"><div class="img" role="img" aria-label="Product photo: white supplement jar with green label"><span style="background:linear-gradient(180deg,#f5f5f5 0 25%,#6aa85a 25% 70%,#f5f5f5 70%)"></span></div><div class="meta"><div class="stars">★★★★<b>★</b></div><div class="pname">Cannabis Product</div><div class="price">$500.00</div><div class="swatches"><i style="background:var(--sw1)"></i><i style="background:var(--sw2)"></i><i style="background:var(--sw3)"></i></div></div></div>
  <div class="card" style="left:591px;top:535px"><div class="img" role="img" aria-label="Product photo: grey box with yellow warning label"><span style="background:linear-gradient(180deg,#555 0 20%,#e8e8e8 20% 60%,#e3c92a 60% 85%,#555 85%)"></span></div><div class="meta"><div class="stars">★★★★<b>★</b></div><div class="pname">Cannabis Product</div><div class="price">$500.00</div><div class="swatches"><i style="background:var(--sw1)"></i><i style="background:var(--sw2)"></i><i style="background:var(--sw3)"></i></div></div></div>
  <div class="card" style="left:679px;top:535px"><div class="img" role="img" aria-label="Product photo: bundle of pre-rolled cones"><span style="background:linear-gradient(160deg,#8a7a5a,#b59a70)"></span></div><div class="meta"><div class="stars">★★★★<b>★</b></div><div class="pname">Cannabis Product</div><div class="price">$500.00</div><div class="swatches"><i style="background:var(--sw1)"></i><i style="background:var(--sw2)"></i><i style="background:var(--sw3)"></i></div></div></div>

  <!-- second product row -->
  <div class="card" style="left:236px;top:710px"><div class="img" role="img" aria-label="Product photo: kraft box and vape cartridge"><span style="background:linear-gradient(90deg,#c8ac86 55%,#e8c02a 55%)"></span></div><div class="meta"><div class="stars">★★★★<b>★</b></div><div class="pname">Cannabis Product</div><div class="price">$500.00</div><div class="swatches"><i style="background:var(--sw1)"></i><i style="background:var(--sw2)"></i><i style="background:var(--sw3)"></i></div></div></div>
  <div class="card" style="left:324px;top:710px"><div class="img" role="img" aria-label="Product photo: orange and white box"><span style="background:linear-gradient(180deg,#f06a3a 0 30%,#f5f5f5 30% 45%,#f06a3a 45%)"></span></div><div class="meta"><div class="stars">★★★★<b>★</b></div><div class="pname">Cannabis Product</div><div class="price">$500.00</div><div class="swatches"><i style="background:var(--sw1)"></i><i style="background:var(--sw2)"></i><i style="background:var(--sw3)"></i></div></div></div>
  <div class="card" style="left:413px;top:710px"><div class="img" role="img" aria-label="Product photo: olive green canister"><span style="background:linear-gradient(180deg,#d8d8d8 0 12%,#6a7a36 12%)"></span></div><div class="meta"><div class="stars">★★★★<b>★</b></div><div class="pname">Cannabis Product</div><div class="price">$500.00</div><div class="swatches"><i style="background:var(--sw1)"></i><i style="background:var(--sw2)"></i><i style="background:var(--sw3)"></i></div></div></div>
  <div class="card" style="left:502px;top:710px"><div class="img" role="img" aria-label="Product photo: orange pouch"><span style="background:linear-gradient(180deg,#f39a2a,#f5f0ea 40%,#f39a2a)"></span></div><div class="meta"><div class="stars">★★★★<b>★</b></div><div class="pname">Cannabis Product</div><div class="price">$500.00</div><div class="swatches"><i style="background:var(--sw1)"></i><i style="background:var(--sw2)"></i><i style="background:var(--sw3)"></i></div></div></div>
  <div class="card" style="left:591px;top:710px"><div class="img" role="img" aria-label="Product photo: single cannabis bud"><span style="background:radial-gradient(circle,#5f8a3a,#3f6a2a 60%,#ececec 72%)"></span></div><div class="meta"><div class="stars">★★★★<b>★</b></div><div class="pname">Cannabis Product</div><div class="price">$500.00</div><div class="swatches"><i style="background:var(--sw1)"></i><i style="background:var(--sw2)"></i><i style="background:var(--sw3)"></i></div></div></div>
  <div class="card" style="left:679px;top:710px"><div class="img" role="img" aria-label="Product photo: orange pouch"><span style="background:linear-gradient(180deg,#f39a2a,#f5f0ea 40%,#f39a2a)"></span></div><div class="meta"><div class="stars">★★★★<b>★</b></div><div class="pname">Cannabis Product</div><div class="price">$500.00</div><div class="swatches"><i style="background:var(--sw1)"></i><i style="background:var(--sw2)"></i><i style="background:var(--sw3)"></i></div></div></div>

  <div class="abs pager">
    <div class="cell" style="left:0;width:24px"><svg width="5" height="7" viewBox="0 0 5 7"><path d="M4 .5L1 3.5 4 6.5" stroke="#aaa" fill="none"/></svg></div>
    <div class="cell" style="left:24px;width:22px;color:#333">1</div>
    <div class="cell" style="left:46px;width:23px">2</div>
    <div class="cell" style="left:69px;width:23px">3</div>
    <div class="cell" style="left:92px;width:24px"><svg width="5" height="7" viewBox="0 0 5 7"><path d="M1 .5L4 3.5 1 6.5" stroke="#ddd" fill="none"/></svg></div>
    <div class="abs" style="left:266px;top:0;width:1px;height:26px;background:var(--line)"></div>
    <div class="result">Showing Products 1-24 of 10 Result</div>
  </div>

  <footer class="abs footer"></footer>
  <div class="fcol logo" style="left:69px;top:1026px;width:140px;font-size:16px">VALE EMBER</div>
  <div class="fcol about" style="left:49px;top:1063px;width:180px;font-size:7px;line-height:16.3px">Lorem ipsum dolor sit amet, consectetur<br>adipiscing elit, sed do eiusmod tempor incididunt<br>ut labore et.Lorem ipsum dolor sit amet,<br>consectetur adipiscing</div>
  <div class="vline" style="left:236px"></div>
  <div class="vline" style="left:575px"></div>
  <div class="fcol" style="left:292px;top:1014px;width:227px;font-size:18.5px;font-weight:700;letter-spacing:.5px">NEWSLETTER</div>
  <div class="abs news-input">Enter your email</div>
  <div class="abs subscribe">SUBSCRIBE</div>
  <div class="fcol" style="left:591px;top:1009px;width:160px;font-size:9.5px;font-weight:700">STORE INFORMATION</div>
  <div class="fcol info" style="left:591px;top:1032px;width:160px">
    <p>Vale Ember Store, Demo store</p>
    <p>USA 123-456</p>
    <p>Call Us: 123-456-7890</p>
    <p>Email Us: info@valeember.com</p>
    <p>Fax: 123456</p>
  </div>
  <div class="abs bottomline"></div>
  <div class="abs" style="left:58px;top:1177px;font-size:7px">© 2020 All Right Reserved</div>
  <div class="pay" style="left:649px;background:#f1f1f1"></div>
  <div class="pay" style="left:671px;background:#f08a4a"></div>
  <div class="pay" style="left:693px;background:#f1f1f1"></div>
  <div class="pay" style="left:714px;background:#3aa6e0"></div>
  <div class="pay" style="left:736px;background:#f1f1f1"></div>

</div>
</body>
</html>
```